Animal Eye Clinic needs a Business card

We are a new veterinary ophthalmology practice (Silverbrook Pet Vision Care) and we need a business card designed. We only see animal eyes - we are not a regular veterinary clinic. We already have a logo. We are looking for a professional, good looking business card to hand out to our clients. We are looking for something simple but professional and contemporary. Our logo is likely the only picture/graphic that needs to be on the card.

Contact Information for Business Card

Marisol Quent, BSc, DVM, MSc, DipACVO
Veterinary Ophthalmologist

Phone: 250.419.3067
Email: silverbrookpetvisioncare@mailvero.com
Website: silverbrookpetvisioncare.com
Address: 1875 Tessock Rd
Kelowna, BC, V4T 8M3

Colors

Designer to choose colors to be used in the design.

Requirements
Must have
• Our logo (attached)

```html
<!DOCTYPE html>
<html lang="en">
<head>
<meta charset="utf-8">
<title>Silverbrook Pet Vision Care — Business Card</title>
<link href="https://fonts.googleapis.com/css2?family=Oswald:wght@500&family=Roboto:wght@300;400;500&display=swap" rel="stylesheet">
<style>
  :root {
    --backdrop: #3a3a3b;
    --card: #2a2a2b;
    --teal: #0a9aae;
    --ink: #eeeeee;
    --muted: #cfcfcf;
  }
  * { box-sizing: border-box; margin: 0; padding: 0; }
  html, body {
    width: 1200px; height: 901px; overflow: hidden;
    background: var(--backdrop);
    font-family: "Roboto", Arial, sans-serif;
  }
  .stage {
    position: relative; width: 1200px; height: 901px;
    display: flex; flex-direction: column; align-items: center; justify-content: center; gap: 40px;
  }
  .card {
    position: relative; width: 640px; height: 366px;
    background: var(--card);
    box-shadow: 0 14px 30px rgba(0,0,0,.35);
    overflow: hidden;
  }
  .card__band {
    position: absolute; left: 0; right: 0; bottom: 0; height: 11px;
    background: var(--teal);
  }
  /* Front */
  .brand {
    position: absolute; left: 0; right: 0; top: 150px;
    display: flex; align-items: center; justify-content: center; gap: 14px;
  }
  .brand__dot {
    width: 34px; height: 34px; border-radius: 50%; background: var(--teal);
  }
  .brand__name {
    font-family: "Roboto", Arial, sans-serif; font-weight: 500;
    font-size: 30px; letter-spacing: .5px; color: var(--teal);
  }
  /* Back */
  .person {
    position: absolute; left: 20px; width: 272px; top: 128px; text-align: right;
  }
  .person__name {
    font-family: "Oswald", "Arial Narrow", sans-serif; font-weight: 500;
    font-size: 15px; color: var(--teal); letter-spacing: .2px; white-space: nowrap;
  }
  .person__title {
    margin-top: 6px; font-size: 15px; font-weight: 300; color: var(--muted);
  }
  .divider {
    position: absolute; left: 304px; top: 126px; width: 1.5px; height: 64px; background: var(--muted);
  }
  .contacts {
    position: absolute; left: 318px; top: 128px; list-style: none;
  }
  .contacts li {
    display: flex; align-items: center; gap: 7px;
    font-size: 13px; font-weight: 300; color: var(--ink); line-height: 20px; white-space: nowrap;
  }
  .contacts svg { width: 12px; height: 12px; flex: none; fill: var(--teal); }
  .contacts .accent { color: var(--teal); }
  .address {
    position: absolute; left: 0; right: 0; top: 286px; text-align: center;
    font-size: 15px; font-weight: 300; color: var(--ink);
  }
</style>
</head>
<body>
<main class="stage">
  <section class="card card--front" aria-label="Card front">
    <div class="brand">
      <span class="brand__dot"></span>
      <span class="brand__name">Silverbrook Pet Vision Care</span>
    </div>
    <div class="card__band"></div>
  </section>

  <section class="card card--back" aria-label="Card back">
    <div class="person">
      <p class="person__name">MARISOL QUENT, BSC, DVM, MSC, DIPACVO</p>
      <p class="person__title">Veterinary Ophthalmologist</p>
    </div>
    <div class="divider"></div>
    <ul class="contacts">
      <li>
        <svg viewBox="0 0 24 24"><path d="M6.6 10.8a15.1 15.1 0 0 0 6.6 6.6l2.2-2.2c.3-.3.7-.4 1-.2 1.1.4 2.3.6 3.6.6.6 0 1 .4 1 1V20c0 .6-.4 1-1 1A17 17 0 0 1 3 4c0-.6.4-1 1-1h3.5c.6 0 1 .4 1 1 0 1.3.2 2.5.6 3.6.1.3 0 .7-.2 1z"/></svg>
        250.419.3067
      </li>
      <li>
        <svg viewBox="0 0 24 24"><path d="M2 5h20v14H2z M2 5l10 8 10-8" fill="none" stroke="#0a9aae" stroke-width="0"/><path d="M2 5h20v1.5l-10 7-10-7z M2 8.5l10 7 10-7V19H2z"/></svg>
        silverbrookpetvisioncare@mailvero.com
      </li>
      <li>
        <svg viewBox="0 0 24 24"><circle cx="12" cy="12" r="9.5" fill="none" stroke="#0a9aae" stroke-width="2.5"/><path d="M12 2.5v19M2.5 12h19" stroke="#0a9aae" stroke-width="2"/></svg>
        <span>www.<span class="accent">silverbrookpetvisioncare</span>.com</span>
      </li>
    </ul>
    <p class="address">1875 Tessock Rd, Kelowna, BC, V4T 8M3</p>
    <div class="card__band"></div>
  </section>
</main>
</body>
</html>
```